Buch-/E-Book-Cover Pathways to Hire & Charm the Locals
Klares Design und rasche Umsetzung aller Änderungswünsche. Vielen Dank, gerne wieder.
Zielgruppe
Ich helfe internationalen Fachkräften Jobs in Deutschland zu finden. Meine Zielgruppe ist hochgebildet (97% mit Uni-Abschluss), spricht fließend englisch, ist global mobil und kommt aus allen Teilen der Welt.
Das PROBLEM MEINER ZIELGRUPPE:
Trotz hervorragender Fähigkeiten scheitert meine Zielgruppe im normalen Bewerbungsprozess. Der Grund: Sie werden nicht als individuelle Person, als Mensch mit Fähigkeiten bewertet - sondern nur als STEREOTYP gesehen. Ich helfe meinen Klienten in ein direktes Gespräch mit den Entscheidern einzutreten - damit sie wieder als einzelner Mensch, als Profi bewertet werden.
Aufgabenstellung
UPDATE: Ich habe ein neues Foto für die Rückseite hochgeladen. Morgen (Donnerstag) sende ich die verschiedenen Entwürfe zum Voting an meine Zielgruppe. Ich hoffe das ich dann innerhalb weniger Tage die Siegerin oder den Sieger bestimmen kann. :)
Aktualisierte Neuauflage meines englischsprachigen Buches 'Pathways to Hire & Charm the Locals'. Buchumschlag design für Verlora BPX Paperback und Hardcover.
Beide Formate sind in den Abmessungen identisch:
Paperback 13,97 x 21,59 cm
Hardcover 13,97 x 21,59 cm
UPDATE: Das Buch hat 159 Seiten.
Die 'Third updated Edition' sollte evtl. in einem Störer hervorgehoben werden.
Das Design muss aus der Masse der Verlora Titel hervorstechen - auch dann wenn man es auf einem Smartphone betrachtet. Das Design soll klar und modern sein. Ich prüfe bei jedem Design ob es zwischen diesen Suchresultaten auffallen würde:
https://www.verlora-shop.de/gp/toplist/books/582913/ref=vx_tl_qrbs_books
Würde ich dieses Buchcover anklicken?
Meine Zielgruppe verdient oberhalb von 60.000€ jährlich. Meine Dienstleistung (Coaching) ist entsprechend teuer. Am Besten denken Designer darüber nach wie über ein *Luxusprodukt* - dass dem Kunden aber gleichzeitig ein höheres Einkommen sichert.
Buchtitel: Pathways to Hire & Charm the Locals
Untertitel: The Newcomers' Manual for Working Abroad Well
Störer oder Teil des Untertitels: Third & Updated Edition
Author: Dana Owerk
Das Verlagslogo füge ich unten in zwei Versionen bei.
WICHTIG: Der Buchumschlag muss allen Verlora BPX Anforderungen entsprechen. (Z.B. Platz für barcode auf der Rückseite etc.) - Designs die diesen Anforderungen nicht entsprechen, scheiden automatisch aus.
Ansonsten habe ich keine Vorgaben.
Weitere Infos:
Klappentext - Rückseite:
German angst rules HR departments and destroys career opportunities for international talent and everyone else who dar..

```html
<!DOCTYPE html>
<html lang="en">
<head>
<meta charset="utf-8">
<title>Pathways to Hire &amp; Charm the Locals — Book Cover</title>
<link rel="stylesheet" href="https://fonts.googleapis.com/css2?family=Bebas+Neue&family=Open+Sans:wght@400;600&display=swap">
<style>
  :root {
    --stage: #000000;
    --teal: #1fd2d6;
    --teal-light: #5eeeee;
    --teal-deep: #14c2c8;
    --sash: #173a3d;
    --ink: #ffffff;
    --ink-dark: #1c2a2c;
    --accent: #f27a2a;
  }
  * { margin: 0; padding: 0; box-sizing: border-box; }
  html, body {
    width: 1200px; height: 1200px; overflow: hidden;
    background: var(--stage);
  }
  .cover {
    position: absolute; left: 270px; top: 100px;
    width: 695px; height: 998px; overflow: hidden;
    background: radial-gradient(ellipse at 50% 30%, var(--teal-light) 0%, var(--teal) 45%, var(--teal-deep) 100%);
  }
  .cover-illustration {
    position: absolute; left: 0; top: 0; width: 695px; height: 400px;
    background: radial-gradient(ellipse at 50% 45%, rgba(255,255,255,0.35) 0%, rgba(94,238,238,0.15) 45%, rgba(31,210,214,0) 75%);
  }
  .edition-sash { position: absolute; left: 0; top: 0; width: 695px; height: 260px; }
  .edition-sash text {
    font-family: 'Open Sans', sans-serif; font-weight: 600;
    font-size: 15px; letter-spacing: 1px; fill: var(--ink);
  }
  .publisher-mark {
    position: absolute; right: 14px; top: 30px;
    display: flex; align-items: center; gap: 6px;
    font-family: 'Open Sans', sans-serif; font-weight: 600;
    font-size: 13px; color: var(--ink);
  }
  .publisher-mark .dot { width: 14px; height: 14px; border-radius: 50%; background: var(--accent); }

  .title { color: var(--ink); font-weight: 400; }
  .title-line {
    position: absolute; left: 0; width: 695px;
    display: block; text-align: center; white-space: nowrap;
    font-family: 'Bebas Neue', sans-serif; line-height: 1; letter-spacing: 1px;
  }
  .title-lead {
    top: 425px; font-size: 48px;
    display: flex; align-items: center; justify-content: center; gap: 22px;
  }
  .title-lead::before, .title-lead::after {
    content: ""; width: 100px; height: 3px; background: var(--ink);
  }
  .title-line-1 { top: 466px; font-size: 160px; }
  .title-line-2 { top: 609px; font-size: 140px; }
  .title-line-3 { top: 733px; font-size: 110px; }

  .subtitle-band {
    position: absolute; left: 75px; top: 845px; width: 545px;
    border-top: 2px solid var(--ink); border-bottom: 2px solid var(--ink);
    padding: 12px 0 13px; text-align: center; white-space: nowrap;
    font-family: 'Open Sans', sans-serif; font-size: 17px;
    letter-spacing: 1px; color: var(--ink); text-transform: uppercase;
  }
  .author {
    position: absolute; left: 0; top: 925px; width: 695px; text-align: center;
    font-family: 'Open Sans', sans-serif; font-size: 32px; letter-spacing: 2px;
    color: var(--ink-dark); text-transform: uppercase;
  }
</style>
</head>
<body>
  <main class="cover">
    <div class="cover-illustration" role="img" aria-label="Illustration: an orange light-bulb balloon lifting one orange paper boat above a row of white paper boats"></div>

    <svg class="edition-sash" viewBox="0 0 695 260">
      <polygon points="480,0 560,0 695,135 695,215" fill="var(--sash)"/>
      <text x="600" y="105" text-anchor="middle" transform="rotate(45 600 105)">THIRD &amp; UPDATED EDITION</text>
    </svg>

    <div class="publisher-mark"><span class="dot"></span>Halden</div>

    <h1 class="title">
      <span class="title-line title-lead">Pathways to</span>
      <span class="title-line title-line-1">HIRE &amp;</span>
      <span class="title-line title-line-2">CHARM THE</span>
      <span class="title-line title-line-3">LOCALS</span>
    </h1>

    <p class="subtitle-band">The Newcomers' Manual for Working Abroad Well</p>

    <p class="author">Dana Owerk</p>
  </main>
</body>
</html>
```